Responsive WordPress website for medical therapy practice consulting business.

We need both design and website for responsive Wordpress website. The use of Tessaly theme is preferred when considering the design (not required).
Site must be designed for 1920px width and fully responsive.
See full scope of the project below.

DESIGN:
Design a full screen layout using images and parallax movement where appropriate.
Easy to use navigation for desktop and hamburger style navigation for mobile devices.
Create an original design for the home, sub-page template.
Create a responsive website using common desktop breakpoints 1920, 1366, 1280 1024 as well as mobile devices.
Color scheme should use soft or pastel color avoiding reds.
Design will take inspiration from logo design and color scheme.
Large “Hero slider” may be employed to striking visual interest.
The website will focus the content on the Homepage mission statement, What We Do and How to Reach Us, content.
Website Footer Information: Include content for Privacy Policy and Terms of Use, address and copyright information.

DEVELOPMENT NOTES:

WordPress content management platform will be used .

Responsive grid will be used to properly display website content on all devices including mobile, laptop and desktop at standard breakpoints.

Social Media links to LinkedIn and Twitter

Google Analytics and Search Console integration – allows tracking of visitors and in-depth search data, indexing and performance.

Yoast Basic SEO – basic setup and integration is included in the proposal. This includes creating SEO friendly page titles, search descriptions and best practices for heading and image tags.

508 & ADA compliance

PAGE LIST:
The following pages are a list of current websites pages. These are used as a guideline for developing the proposal and can be changed to reflect content:

NAVIGATION LINKS:

HOME

· Featuring the new logo, the home page will display Brenlow Care Advisor’s message, services, and contact information.
· The navigation will be prominent, intuitive and easy to use, allowing to find information quickly.
· Parallax scrolling will provide a cool modern visual effect without being overbearing.

====================================================

ABOUT US –

· History
· Bios
· Links

SERVICES

· Business Consultancy service

CONTACT US – This section will present ways for viewers to reach out either by phone, email.

· Google map of office locations.
· Business information
a. Locations
b. Address
c. Phone
d. Fax
e. Email

FOOTER LINKS – Additional information for legal or usage claims, company info and contact info.

· Copyright information
· Links to CONTACT
· Social Media
· Disclaimer
· Privacy policy
· Terms of use

```html
<!DOCTYPE html>
<html lang="en">
<head>
<meta charset="utf-8">
<title>Brenlow Care Advisors</title>
<link href="https://fonts.googleapis.com/css2?family=Roboto:wght@300;400;500;700;900&display=swap" rel="stylesheet">
<style>
:root{
  --blue:#1e88e5;
  --blue-dark:#1565c0;
  --blue-light:#2b9fe6;
  --sky:#cfe8fb;
  --ink:#2b2b2b;
  --text:#6d7680;
  --panel:#f2f4f6;
  --charcoal:#4a4a4a;
  --footer:#2b2b2b;
  --white:#fff;
}
*{box-sizing:border-box;margin:0;padding:0}
html,body{width:1200px;height:2788px;overflow:hidden}
body{font-family:'Roboto',sans-serif;color:var(--ink);background:var(--white);position:relative}
section,header,footer{position:absolute;left:0;width:1200px}

/* hero */
.hero{top:0;height:600px;background:#e4ebf1}
.hero-photo{position:absolute;inset:0;
  background:
    radial-gradient(ellipse 220px 300px at 50% 62%,rgba(255,255,255,.95) 0%,rgba(255,255,255,0) 100%),
    radial-gradient(ellipse 160px 200px at 50% 28%,rgba(236,205,150,.85) 0%,rgba(236,205,150,0) 100%),
    radial-gradient(ellipse 180px 260px at 86% 60%,rgba(170,205,232,.9) 0%,rgba(170,205,232,0) 100%),
    radial-gradient(ellipse 160px 240px at 16% 62%,rgba(190,215,236,.85) 0%,rgba(190,215,236,0) 100%),
    radial-gradient(ellipse 140px 200px at 30% 45%,rgba(214,190,160,.55) 0%,rgba(214,190,160,0) 100%),
    linear-gradient(180deg,#dfe7ee 0%,#cfdae4 60%,#eef2f6 100%);}
.topbar{position:absolute;top:0;left:0;width:1200px;height:80px;background:rgba(255,255,255,.9);display:flex;align-items:center;justify-content:space-between;padding:0 160px}
.brand{display:flex;align-items:center;gap:12px;font-weight:700;font-size:22px;color:var(--blue-dark)}
.brand-mark{width:34px;height:34px;background:var(--blue)}
.nav{display:flex;gap:28px;font-size:13px;font-weight:500;color:var(--ink)}

/* practice area */
.practice{top:600px;height:410px;text-align:center}
.section-title{font-size:44px;font-weight:900;letter-spacing:1px;color:var(--ink)}
.section-sub{font-size:26px;font-weight:400;color:var(--blue)}
.practice .section-title{margin-top:40px}
.cards{display:flex;justify-content:center;gap:56px;margin-top:36px}
.card{width:232px;height:238px;background:var(--panel);padding:24px 20px;text-align:center}
.card svg{width:48px;height:48px}
.card h3{font-size:15px;font-weight:700;color:var(--blue);margin:14px 0 10px}
.card p{font-size:11px;line-height:1.6;color:var(--text)}

/* mission */
.mission{top:1020px;height:360px;background:var(--blue-dark)}
.mission-copy{position:absolute;left:0;top:0;width:480px;height:360px;background:var(--blue-light);padding:64px 24px 0 160px;color:var(--white)}
.mission-copy h2{font-size:25px;font-weight:900;color:var(--ink);margin-bottom:14px;white-space:nowrap}
.mission-copy p{font-size:11px;line-height:1.65}
.arrows{display:flex;gap:6px;margin-top:18px}
.arrows span{width:24px;height:24px;border:1px solid var(--white);display:flex;align-items:center;justify-content:center}
.mission-cards{position:absolute;left:500px;top:80px;display:flex;gap:12px}
.mcard{width:220px;height:200px;background:var(--white);padding:6px}
.mcard .ph{height:150px}
.ph-a{background:radial-gradient(ellipse at 45% 45%,#e9d2b6 0%,#c9d8e4 55%,#9fb6c8 100%)}
.ph-b{background:radial-gradient(ellipse at 55% 50%,#f3f6f8 0%,#cfe0ea 50%,#a9c3d4 100%)}
.ph-c{background:radial-gradient(ellipse at 40% 50%,#e6d8c8 0%,#d6e2ea 50%,#8fa9bd 100%)}
.mcard b{display:block;text-align:center;font-size:11px;font-weight:700;color:var(--blue-dark);margin-top:14px}

/* what we do */
.whatwedo{top:1380px;height:420px;text-align:center}
.whatwedo .section-title{margin-top:50px}
.intro{width:760px;margin:14px auto 0;font-size:11px;line-height:1.65;color:var(--text)}
.timeline{position:absolute;left:0;top:190px;width:1200px;height:200px}
.step-label{position:absolute;top:100px;width:140px;font-size:11px;font-weight:500;color:var(--ink);line-height:1.4}

/* reach */
.reach{top:1800px;height:520px;background:linear-gradient(180deg,#eef1f4,#e3e8ec);text-align:center}
.reach .section-title{margin-top:50px}
.contact-box{position:absolute;left:180px;top:200px;width:840px;height:280px;background:var(--blue-dark);display:flex;color:var(--white)}
.contact-col{flex:1;text-align:center;padding-top:40px}
.contact-col svg{width:34px;height:34px}
.contact-col h4{font-size:17px;font-weight:400;margin:12px 0 14px}
.contact-col p{font-size:13px;line-height:1.55}
.contact-col .strong{font-weight:700}
.contact-col .link{margin-top:26px;font-size:13px}

/* contact form */
.contact{top:2320px;height:400px;background:var(--charcoal);text-align:center}
.contact .section-title{color:var(--white);font-size:38px;margin-top:44px}
.form{position:absolute;left:180px;top:130px;width:840px}
.row{display:flex;gap:20px}
.field{flex:1;height:34px;border:1px solid #7a7a7a;background:#555;color:#bbb;font-size:11px;text-align:left;padding:10px 12px}
.message{height:120px;margin-top:18px;flex:none;width:100%}
.submit{display:inline-block;margin-top:22px;background:var(--footer);color:var(--white);font-weight:700;font-size:13px;padding:10px 34px}

/* footer */
.site-footer{top:2720px;height:68px;background:var(--footer);color:#bbb;padding:14px 160px;font-size:10px}
.footer-links{display:flex;gap:22px;font-weight:500}
.copyright{margin-top:8px;color:#888}
.social{position:absolute;right:160px;top:22px;display:flex;gap:10px}
.social span{width:22px;height:22px;border-radius:50%;border:1px solid #bbb}
</style>
</head>
<body>

<header class="hero">
  <div class="hero-photo" role="img" aria-label="Smiling team of medical therapy professionals in white coats and blue scrubs"></div>
  <div class="topbar">
    <div class="brand"><span class="brand-mark"></span>Brenlow Care Advisors</div>
    <nav class="nav"><span>HOME</span><span>ABOUT US</span><span>SERVICES</span><span>CONTACT US</span></nav>
  </div>
</header>

<section class="practice">
  <h2 class="section-title">OUR</h2>
  <div class="section-sub">Therapy Practice Area</div>
  <div class="cards">
    <article class="card">
      <svg viewBox="0 0 48 48" fill="none" stroke="#2b2b2b" stroke-width="2"><rect x="8" y="26" width="32" height="8"/><circle cx="16" cy="18" r="5"/><path d="M22 22h14M10 34v6M38 34v6"/></svg>
      <h3>Practice Operations</h3>
      <p>Our advisors review intake, billing and scheduling so therapy teams spend more time with patients and less time on paperwork.</p>
    </article>
    <article class="card">
      <svg viewBox="0 0 48 48" fill="none" stroke="#2b2b2b" stroke-width="2"><circle cx="24" cy="14" r="7"/><path d="M10 42c0-9 6-15 14-15s14 6 14 15z"/><path d="M24 30v8M20 34h8"/></svg>
      <h3>Clinical Staffing</h3>
      <p>We guide hiring, onboarding and retention so every clinic keeps skilled therapists and a calm, well supported team.</p>
    </article>
    <article class="card">
      <svg viewBox="0 0 48 48" fill="none" stroke="#2b2b2b" stroke-width="2"><path d="M10 26h28v6a10 10 0 0 1-10 10h-8a10 10 0 0 1-10-10z"/><path d="M30 8l-8 16M24 10h8v8"/></svg>
      <h3>Revenue Growth</h3>
      <p>Clear reporting and smarter coding help practices track results, reduce denials and plan growth with confidence.</p>
    </article>
  </div>
</section>

<section class="mission">
  <div class="mission-copy">
    <h2>MISSION STATEMENT</h2>
    <p>We help therapy practices grow with steady guidance on operations, staffing, compliance and patient experience. Our advisors work beside owners to turn daily challenges into clear plans, measurable goals and lasting results for every clinic we serve.</p>
    <div class="arrows">
      <span><svg width="10" height="10" viewBox="0 0 10 10" fill="none" stroke="#fff" stroke-width="1.5"><path d="M7 1L3 5l4 4"/></svg></span>
      <span><svg width="10" height="10" viewBox="0 0 10 10" fill="none" stroke="#fff" stroke-width="1.5"><path d="M3 1l4 4-4 4"/></svg></span>
    </div>
  </div>
  <div class="mission-cards">
    <div class="mcard"><div class="ph ph-a" role="img" aria-label="Therapist meeting with a patient"></div><b>PATIENT EXPERIENCE</b></div>
    <div class="mcard"><div class="ph ph-b" role="img" aria-label="Physical therapy session in a bright clinic"></div><b>CLINIC WORKFLOW</b></div>
    <div class="mcard"><div class="ph ph-c" role="img" aria-label="Consultant reviewing notes with clinic staff"></div><b>TEAM TRAINING</b></div>
  </div>
</section>

<section class="whatwedo">
  <h2 class="section-title">WHAT WE DO</h2>
  <p class="intro">We partner with clinics of every size to improve workflows, strengthen finances and build teams that deliver consistent, compassionate care. Each engagement begins with listening and ends with practical steps your staff can follow.</p>
  <div class="timeline">
    <svg width="1200" height="100" viewBox="0 0 1200 100">
      <line x1="180" y1="50" x2="1020" y2="50" stroke="#3a4550" stroke-width="2"/>
      <circle cx="180" cy="50" r="5" fill="#3a4550"/><circle cx="1020" cy="50" r="5" fill="#3a4550"/>
      <circle cx="370" cy="50" r="4" fill="#3a4550"/><circle cx="590" cy="50" r="4" fill="#3a4550"/><circle cx="810" cy="50" r="4" fill="#3a4550"/>
      <g fill="#cfe8fb" stroke="#9ccdf2" stroke-width="2">
        <circle cx="260" cy="50" r="40"/><circle cx="480" cy="50" r="40"/><circle cx="700" cy="50" r="40"/><circle cx="920" cy="50" r="40"/>
      </g>
      <g fill="none" stroke="#1565c0" stroke-width="2.5">
        <rect x="246" y="36" width="26" height="26"/><circle cx="262" cy="50" r="6"/><path d="M266 54l8 8"/>
        <circle cx="480" cy="40" r="6"/><path d="M468 64c0-9 5-14 12-14s12 5 12 14z"/>
        <path d="M688 38h24l-4 26h-16z"/><path d="M700 44v12M694 50h12"/>
        <rect x="906" y="40" width="28" height="22"/><path d="M914 40v-5h12v5M920 46v10M915 51h10"/>
      </g>
    </svg>
    <div class="step-label" style="left:190px">PRACTICE<br>ASSESSMENT</div>
    <div class="step-label" style="left:410px">STAFF<br>DEVELOPMENT</div>
    <div class="step-label" style="left:630px">CARE<br>PLANNING</div>
    <div class="step-label" style="left:850px">HEALTH<br>COMPLIANCE</div>
  </div>
</section>

<section class="reach" role="img" aria-label="Soft grey street map of the office area behind the contact details">
  <h2 class="section-title">HOW TO REACH US</h2>
  <p class="intro">Whether you run a single clinic or a growing group, our team is ready to talk through your goals. Call, write or visit our office and we will respond within one business day with next steps.</p>
  <div class="contact-box">
    <div class="contact-col">
      <svg viewBox="0 0 34 34" fill="#fff"><path d="M17 2a10 10 0 0 0-10 10c0 8 10 20 10 20s10-12 10-20A10 10 0 0 0 17 2zm0 14a4 4 0 1 1 0-8 4 4 0 0 1 0 8z"/></svg>
      <h4>Our Address</h4>
      <p class="strong">Brenlow Care Advisors</p>
      <p>1200 Harbor Point Avenue, Suite 310<br>Tessaly FL 33458</p>
      <p class="link">→ Directions</p>
    </div>
    <div class="contact-col">
      <svg viewBox="0 0 34 34" fill="#fff"><path d="M9 3l5 7-3 3a16 16 0 0 0 10 10l3-3 7 5-3 5C15 30 4 19 4 6z"/></svg>
      <h4>Phone</h4>
      <p class="strong" style="font-size:16px">(555) 014 2290</p>
      <p class="link" style="margin-top:44px">→ Call To Us</p>
    </div>
    <div class="contact-col">
      <svg viewBox="0 0 34 34" fill="#fff"><path d="M3 7h28v20H3z" opacity=".9"/><path d="M3 7l14 11L31 7" fill="none" stroke="#1565c0" stroke-width="2"/></svg>
      <h4>Email</h4>
      <p>hello@brenlowcare.com</p>
      <p class="link" style="margin-top:44px">→ Send Message</p>
    </div>
  </div>
</section>

<section class="contact">
  <h2 class="section-title">CONTACT US</h2>
  <div class="form">
    <div class="row"><div class="field">Name</div><div class="field">Phone</div><div class="field">Email</div></div>
    <div class="row"><div class="field message">Message</div></div>
    <span class="submit">SUBMIT</span>
  </div>
</section>

<footer class="site-footer">
  <div class="footer-links"><span>HOME</span><span>ABOUT US</span><span>SERVICES</span><span>CONTACT US</span><span>PRIVACY POLICY</span><span>TERMS OF USE</span><span>DISCLAIMER</span></div>
  <div class="copyright">Copyright © 2024 Brenlow Care Advisors. All Rights Reserved.</div>
  <div class="social"><span></span><span></span><span></span></div>
</footer>

</body>
</html>
```